Hair Salon Brochure

We need a brochure for our hair salon located in Middle Tennessee called Delphine Locks of Harbor Bend. Along with standard services, we offer specialized services and accommodations for individuals on the Autism Spectrum, regardless of background or hair type.
At Delphine Locks of Harbor Bend, our mission is to create a warm and inclusive haven for individuals of all backgrounds, including those on the autism spectrum and their families. We are dedicated to providing not only exceptional hairstyling services but also hands-on education and specialized cutting techniques for clients with natural textured hair. Our goal is to empower our clients with the knowledge and tools necessary to maintain a successful hair care routine, ensuring they leave our salon feeling confident.
We believe in fostering a sense of community, where parents of younger clients are encouraged to learn the proper hair care techniques for their children, promoting healthy practices at home. Our commitment extends beyond just hair; we are here to help you embrace your true self and recognize the beauty that resides within.
At Delphine Locks of Harbor Bend, our passion is to deliver the ultimate client experience, where you can be unapologetically yourself and feel completely at ease. From the moment you step through our doors, you are welcomed not only to discuss your hair concerns but also to engage in meaningful conversations about life. Together, we will collaborate on a personalized plan to achieve your hair goals and transform the way you perceive yourself.
Always remember, when you look good, you feel good, and when you feel good, you can achieve great things. We firmly believe that every individual is 'Beautiful Beyond the Spectrum,' and we are here to celebrate that beauty with you."
https://www.delphinelocks.net/
Tagline - "Beautiful Beyond the Spectrum"

```html
<!DOCTYPE html>
<html lang="en">
<head>
<meta charset="utf-8">
<title>Delphine Locks of Harbor Bend — Brochure</title>
<link rel="stylesheet" href="https://fonts.googleapis.com/css2?family=Kaushan+Script&family=Quicksand:wght@300;400;500;600;700&display=swap">
<style>
  :root{
    --blue:#1f5fb0;
    --blue-dark:#174a8c;
    --orange:#d9581d;
    --paper:#ffffff;
    --canvas:#e9e9eb;
    --photo-a:#6b5344;
    --photo-b:#2a2527;
  }
  *{margin:0;padding:0;box-sizing:border-box}
  html,body{width:765px;height:1200px;overflow:hidden;background:var(--canvas)}
  body{position:relative;font-family:"Quicksand",sans-serif;color:var(--blue)}
  .sheet{position:absolute;left:20px;width:725px;height:516px;background:var(--paper);overflow:hidden}
  .sheet--outside{top:44px}
  .sheet--inside{top:638px}
  .abs{position:absolute}
  .script{font-family:"Kaushan Script",cursive;color:var(--orange);font-weight:400}
  .script-title{font-size:21px;line-height:1;padding-bottom:4px;border-bottom:1.5px solid var(--blue);display:inline-block}
  svg.deco{position:absolute;left:0;top:0}

  /* outside */
  .mission{left:15px;top:26px;width:212px}
  .mission p{font-size:8.1px;line-height:11.2px;font-weight:400;margin-top:11px}
  .mission p:first-of-type{margin-top:14px}
  .brand{left:255px;top:62px;width:205px;text-align:center}
  .brand-mark{display:inline-block;width:18px;height:18px;border-radius:50%;background:var(--blue);vertical-align:middle;margin-right:6px}
  .brand-name{font-size:17px;font-weight:600;color:var(--blue);line-height:1.25;display:inline-block;vertical-align:middle;text-align:left}
  .contact{left:243px;top:165px;width:230px;text-align:center}
  .contact .script-title{font-size:22px;padding:0 6px 4px}
  .contact h3{font-size:12.5px;font-weight:500;color:var(--orange);margin-top:14px;line-height:1.2}
  .contact h3:first-of-type{margin-top:24px}
  .contact p{font-size:11px;font-weight:500;line-height:14px;margin-top:2px;white-space:nowrap}
  .tagline{left:500px;top:320px;width:215px;text-align:center}
  .tagline .big{font-family:"Kaushan Script",cursive;font-size:34px;color:var(--blue);line-height:1.1}
  .tagline .sub{font-size:17px;font-weight:500;color:var(--orange);margin-top:4px}
  .tagline .note{font-size:7.3px;line-height:10.2px;margin-top:18px}
  .book{left:500px;top:464px;width:215px;text-align:center;font-weight:500}
  .book .label{font-size:13px}
  .book .phone{font-size:15.5px;margin-top:2px}

  /* inside */
  .services{left:17px;top:30px;width:220px}
  .services ul{list-style:none;margin-top:10px;margin-left:-17px;width:237px}
  .services li{font-size:12.4px;font-weight:500;line-height:14.5px;padding:3px 0 4px 17px;border-bottom:1px solid #8fb0dc}
  .special{left:245px;top:16px;width:240px}
  .special h2,.goal h2{font-size:14px;font-weight:600;color:var(--orange);line-height:14.5px;letter-spacing:.2px}
  .special h2{margin-top:12px}
  .q{font-size:9.6px;font-weight:600;line-height:12px;margin-top:5px}
  .body-copy{font-size:9.4px;font-weight:300;line-height:12.2px;margin-top:7px}
  .sign{font-size:11.6px;font-weight:500;line-height:14px;margin-top:10px}
  .goal{left:497px;top:128px;width:212px}
  .brand-small{left:600px;top:454px;text-align:center;width:110px}
  .brand-small .brand-name{font-size:12px;text-align:center}
</style>
</head>
<body>

<section class="sheet sheet--outside">
  <svg class="deco" width="725" height="516" viewBox="0 0 725 516">
    <defs>
      <linearGradient id="photoOut" x1="0" y1="0" x2="1" y2="1">
        <stop offset="0" stop-color="#8c7464"/>
        <stop offset=".45" stop-color="#6b5344"/>
        <stop offset="1" stop-color="#2a2527"/>
      </linearGradient>
      <linearGradient id="photoIn" x1="0" y1="0" x2=".6" y2="1">
        <stop offset="0" stop-color="#7a5d4c"/>
        <stop offset=".5" stop-color="#6b5344"/>
        <stop offset="1" stop-color="#2a2527"/>
      </linearGradient>
    </defs>
    <path d="M426 0 C468 20 476 90 478 150 C482 222 516 268 598 287 C650 298 690 300 725 314 L725 0 Z" fill="var(--blue-dark)"/>
    <path d="M436 0 C474 22 484 90 486 148 C490 216 522 260 602 278 C652 289 692 291 725 304 L725 0 Z" fill="var(--blue)"/>
    <path role="img" aria-label="Portrait photo of the salon owner smiling in a black salon jacket" d="M448 0 C484 24 494 90 496 146 C500 208 530 250 606 268 C654 279 694 282 725 294 L725 0 Z" fill="url(#photoOut)"/>
    <path d="M244 516 C270 470 320 450 360 432 C400 414 420 440 450 470 C475 495 495 510 512 516 Z" fill="var(--blue-dark)"/>
    <path d="M244 516 C270 474 318 456 356 440 C392 426 412 448 438 476 C458 498 476 510 490 516 Z" fill="var(--blue)"/>
  </svg>

  <div class="abs mission">
    <h2 class="script script-title">Our mission</h2>
    <p>At Delphine Locks of Harbor Bend, our mission is to create a warm and inclusive haven for individuals of all backgrounds, including those on the autism spectrum and their families. We are dedicated to providing not only exceptional hairstyling services but also hands-on education and specialized cutting techniques for clients with natural textured hair. Our goal is to empower our clients with the knowledge and tools necessary to maintain a successful hair care routine, ensuring they leave our salon feeling confident.</p>
    <p>We believe in fostering a sense of community, where parents of younger clients are encouraged to learn the proper hair care techniques for their children, promoting healthy practices at home. Our commitment extends beyond just hair; we are here to help you embrace your true self and recognize the beauty that resides within.</p>
    <p>At Delphine Locks of Harbor Bend, our passion is to deliver the ultimate client experience, where you can be unapologetically yourself and feel completely at ease. From the moment you step through our doors, you are welcomed not only to discuss your hair concerns but also to engage in meaningful conversations about life. Together, we will collaborate on a personalized plan to achieve your hair goals and transform the way you perceive yourself.</p>
    <p>Always remember, when you look good, you feel good, and when you feel good, you can achieve great things. We firmly believe that every individual is 'Beautiful Beyond the Spectrum,' and we are here to celebrate that beauty with you."</p>
  </div>

  <div class="abs brand">
    <span class="brand-mark"></span><span class="brand-name">Delphine Locks<br>of Harbor Bend</span>
  </div>

  <div class="abs contact">
    <h2 class="script script-title">Contact Us</h2>
    <h3>Location</h3>
    <p>Delphine Locks of Harbor Bend<br>418 Harbor Bend Pkwy Suite 12<br>HARBOR BEND, Tennessee 37000</p>
    <h3>Opening Hours</h3>
    <p>Thursday and Friday: 8.00 am - 1.00 pm<br>Saturday : 7.00 am - 12.00 pm</p>
    <h3>Website</h3>
    <p>www.delphinelocks.net</p>
  </div>

  <div class="abs tagline">
    <div class="big">Beautiful</div>
    <div class="sub">Beyond the Spectrum</div>
    <p class="note">Along with standard services, we offer specialized services and accommodations for individuals on the Autism Spectrum, regardless of background or hair type.</p>
  </div>

  <div class="abs book">
    <div class="label">BOOK NOW</div>
    <div class="phone">(615) 555-0147</div>
  </div>
</section>

<section class="sheet sheet--inside">
  <svg class="deco" width="725" height="516" viewBox="0 0 725 516">
    <path d="M484 0 C478 40 500 70 560 82 C640 96 690 100 725 140 L725 124 C692 92 645 84 570 72 C510 62 492 34 496 0 Z" fill="var(--blue)"/>
    <path d="M496 0 C494 32 512 58 572 70 C646 84 694 92 725 124 L725 112 C696 82 650 74 580 62 C526 52 508 30 508 0 Z" fill="var(--orange)"/>
    <path d="M0 300 C60 280 120 270 150 292 L150 300 C118 282 62 290 0 310 Z" fill="var(--orange)"/>
    <path d="M150 292 C200 310 240 330 252 380 C260 420 246 480 250 516 L240 516 C236 480 250 420 242 382 C230 336 196 316 150 300 Z" fill="var(--orange)"/>
    <path d="M250 516 C246 480 260 420 252 380 C244 330 210 314 170 298 L178 294 C222 310 256 330 264 380 C272 420 258 480 262 516 Z" fill="var(--blue)"/>
    <path role="img" aria-label="Portrait photo of the stylist smiling in a black salon jacket" d="M40 516 C40 440 60 360 100 300 C130 275 160 285 178 300 C214 318 236 340 240 382 C246 420 232 480 236 516 Z" fill="url(#photoIn)"/>
  </svg>

  <div class="abs services">
    <h2 class="script script-title">Services</h2>
    <ul>
      <li>Specialized Services for Autism Spectrum Individuals:</li>
      <li>Warm and inclusive environment</li>
      <li>Exceptional Hairstyling Services</li>
      <li>Hands-on Education for Natural Textured Hair</li>
      <li>Specialized Cutting Techniques</li>
      <li>Empowerment Through Knowledge and Tools</li>
      <li>Dedication to Client Confidence</li>
    </ul>
  </div>

  <div class="abs special">
    <h2 class="script script-title" style="font-size:22px;color:var(--orange);letter-spacing:0">Special Services</h2>
    <h2>We are not just a salon, we<br>are an experience!</h2>
    <p class="q">Are crowded and noisy hair salon visits causing sensory over load?</p>
    <p class="q">Feeling like the stylist doesn't understand your needs and wish more accommodations were availiabe?</p>
    <p class="q">Parents and Caregivers could you use some time to pamper yourseilf and just to talk with someone who gets it?</p>
    <p class="body-copy">With over 25 years of experience in the hair industry and raising a son on the Autism Spectrum. I understand the need for compassionate sensory friendly hair care services and the benefits to your self esteem. Call for a consultation today to discuss any hair care needs and accp,mmodations that will help provide a better experience. In home services provided.</p>
    <p class="sign">Marisol Fenwick<br>615-555-0147<br>www.delphinelocks.net</p>
  </div>

  <div class="abs goal">
    <h2>Proper hair techniques<br>are our goal.</h2>
    <p class="q">loving Your Hair With DelphineLocks</p>
    <p class="q">Wash days give you anxiety?</p>
    <p class="q">Tired of buying products that end up under the skin?</p>
    <p class="q">Parents do you feel overwhelmed about every aspect of your child's hair?</p>
    <p class="q">Feeling like you need a professional stylist to coach you?</p>
    <p class="body-copy">I am licensed Cosmetologist with over 25 years of experience in the industry speciliazing in natural hair textures ready to help you take charge of your hair. Now offering 1 on 1 classes to address all of the above and more.</p>
    <p class="sign">Lets Chats<br>Marisol Fenwick<br>615-555-0147</p>
  </div>

  <div class="abs brand-small">
    <span class="brand-name">Delphine Locks<br>of Harbor Bend</span>
  </div>
</section>

</body>
</html>
```